Website visual upgrade

I am seeking expressions of interest for the updating the visuals of my website www.lornhavenstaffing.net
I am basically seeking a simple,bold and visually strong graphic makeover.using existing or shortly to be modified text.

```html
<!DOCTYPE html>
<html lang="en">
<head>
<meta charset="utf-8">
<title>Lornhaven Staffing</title>
<link href="https://fonts.googleapis.com/css2?family=Roboto:wght@400;500&family=Open+Sans:wght@400&display=swap" rel="stylesheet">
<style>
:root{
  --brand-red:#c8102e;
  --nav-red:#cc1538;
  --ink:#2b2b2b;
  --text:#333333;
  --frame:#cfcfcf;
  --panel:#efefef;
  --button:#231f20;
  --footer:#2a2a2a;
  --footer-text:#a9a9a9;
}
*{margin:0;padding:0;box-sizing:border-box}
html,body{width:1200px;height:1048px;overflow:hidden;background:#fff}
body{position:relative;font-family:'Roboto',sans-serif;color:var(--text)}
.site-header{position:absolute;left:0;top:0;width:1200px;height:86px;background:linear-gradient(90deg,#ececec 0%,#fafafa 50%,#ececec 100%)}
.brand{position:absolute;left:120px;top:22px;display:flex;align-items:center;gap:12px}
.brand-mark{width:22px;height:22px;border-radius:50%;background:var(--ink)}
.brand-name{font-family:'Roboto',sans-serif;font-weight:500;font-size:32px;color:var(--brand-red);letter-spacing:.5px}
.header-phone{position:absolute;right:118px;top:32px;display:flex;align-items:center;gap:10px;font-size:23px;color:var(--ink);letter-spacing:.5px}
.main-nav{position:absolute;left:120px;top:86px;width:960px;height:50px;background:var(--nav-red);display:flex;align-items:center;justify-content:space-between;padding:0 18px}
.main-nav a{color:#fff;text-decoration:none;font-size:12px;font-weight:500;letter-spacing:.4px;text-transform:uppercase}
.hero{position:absolute;left:120px;top:140px;width:960px;height:412px;border:2px solid var(--frame);background:linear-gradient(120deg,#dfe6e4 0%,#c9c4bf 35%,#e6e2de 60%,#d8c9c8 80%,#eef0ee 100%)}
.hero-controls{position:absolute;left:563px;top:535px;display:flex;gap:11px}
.hero-arrow{width:32px;height:32px;border-radius:50%;background:linear-gradient(#ffffff,#e3e3e3);box-shadow:0 1px 3px rgba(0,0,0,.35);display:flex;align-items:center;justify-content:center}
.feature{position:absolute;top:596px;width:288px;text-align:center}
.feature-title{font-size:20px;font-weight:400;color:var(--brand-red);letter-spacing:.5px;height:40px}
.feature-photo{width:286px;height:141px;border:2px solid var(--frame);margin:0 auto}
.feature-text{font-family:'Open Sans',sans-serif;font-size:13px;line-height:20px;color:var(--text);margin-top:12px}
.read-more{display:inline-block;margin-top:23px;width:110px;height:36px;line-height:36px;background:var(--button);color:#fff;font-size:13px;border-radius:3px;text-decoration:none}
.support-panel{width:286px;height:272px;background:var(--panel);margin:0 auto;padding-top:14px}
.partner-badge{margin:0 auto;background:#fff;border:1px solid #9a9a9a}
.partner-text{font-family:'Open Sans',sans-serif;font-size:12.5px;line-height:18px;color:var(--text);padding:0 6px;margin-top:8px;white-space:nowrap}
.panel-divider{width:262px;height:1px;background:#d6d6d6;margin:11px auto 10px}
.site-footer{position:absolute;left:0;top:928px;width:1200px;height:120px;background:var(--footer);border-top:3px solid var(--brand-red)}
.copyright{position:absolute;left:51px;top:37px;font-size:12px;color:var(--footer-text);letter-spacing:.3px}
.copyright strong{color:#e8e8e8;font-weight:400}
.footer-links{position:absolute;left:51px;top:63px;font-size:12px;color:var(--footer-text);letter-spacing:.3px}
.social{position:absolute;right:129px;top:45px;display:flex;align-items:center;gap:8px;font-size:13px;color:var(--footer-text)}
.social-dot{width:32px;height:32px;border-radius:50%;background:#8a8a8a}
.social-label{margin-right:6px}
</style>
</head>
<body>
<header class="site-header">
  <div class="brand"><span class="brand-mark"></span><span class="brand-name">Lornhaven Staffing</span></div>
  <div class="header-phone">
    <svg width="20" height="20" viewBox="0 0 20 20" aria-hidden="true"><rect width="20" height="20" rx="3" fill="#c8102e"/><path d="M7 4c-1.5 1-2 3-1 5.5s3 4.8 5 6c1.5.8 3 .5 3.8-.6l-1.8-2-1.6.8c-1-.6-2.2-2-2.8-3.3l1.2-1.2L8.8 4.4z" fill="#fff"/></svg>
    <span>61-3-95550172</span>
  </div>
</header>
<nav class="main-nav">
  <a href="#">Home</a><a href="#">Who We Are</a><a href="#">Our Approach</a><a href="#">What We Do</a><a href="#">Migration Assistance</a><a href="#">Job Seekers</a><a href="#">Useful Links</a><a href="#">Support</a><a href="#">Contact Us</a>
</nav>
<section class="hero" role="img" aria-label="Team of professionals smiling and shaking hands in a bright office"></section>
<div class="hero-controls">
  <span class="hero-arrow"><svg width="12" height="14" viewBox="0 0 12 14"><path d="M9 1L3 7l6 6" stroke="#333" stroke-width="3" fill="none"/></svg></span>
  <span class="hero-arrow"><svg width="12" height="14" viewBox="0 0 12 14"><path d="M3 1l6 6-6 6" stroke="#333" stroke-width="3" fill="none"/></svg></span>
</div>
<section class="feature" style="left:128px">
  <h2 class="feature-title">WHO WE ARE</h2>
  <div class="feature-photo" role="img" aria-label="Group of business people in suits standing together" style="background:linear-gradient(90deg,#b9b6b4,#e9e6e3 40%,#3b3a40 75%,#8a8c93)"></div>
  <p class="feature-text">Lorem ipsum dolor sit amet, consectetur<br>adipisicing eitseo eiusmod tempor incididunt<br>ut labore et dolore magna aliqua.</p>
  <a class="read-more" href="#">READ MORE</a>
</section>
<section class="feature" style="left:456px">
  <h2 class="feature-title">WHAT WE DO</h2>
  <div class="feature-photo" role="img" aria-label="Seated group meeting with a mentor in an office" style="background:linear-gradient(90deg,#d9d6d0,#8b6d62 35%,#c9c6c0 60%,#4e535a)"></div>
  <p class="feature-text">Lorem ipsum dolor sit amet, consectetur<br>adipisicing eitseo eiusmod tempor incididunt<br>ut labore et dolore magna aliqua.</p>
  <a class="read-more" href="#">READ MORE</a>
</section>
<section class="feature" style="left:783px">
  <h2 class="feature-title">SUPPORT</h2>
  <div class="support-panel">
    <div class="partner-badge" style="width:139px;height:56px"></div>
    <p class="partner-text">Youthlift's mission is to support, develop and<br>empower young people living with cancer.</p>
    <div class="panel-divider"></div>
    <div class="partner-badge" style="width:53px;height:57px;background:#111"></div>
    <p class="partner-text" style="margin-top:15px">The Kinrise Indigenous Fund supports a<br>range of community projects focused on<br>young people in Africa and Australia.</p>
  </div>
</section>
<footer class="site-footer">
  <p class="copyright">Copyright ©2013. <strong>Lornhaven Staffing</strong></p>
  <p class="footer-links">All Right Reserved &nbsp;|&nbsp; Privacy Policy &nbsp;|&nbsp; Site Map</p>
  <div class="social"><span class="social-label">Connect with us:</span><span class="social-dot"></span><span class="social-dot"></span></div>
</footer>
</body>
</html>
```